コンセプトや情報は添付ファイルに書いてますので、それを基に作成お願いします

【注意事項】

※尚、キャバクラやバーにもpopを置くので高級かつ洗練されたデザインを意識してください。

※カラーやフォントの指定はありませんが、いわゆるポスター作成ソフト等によくあるテンプレートを使ったデザインはあまり好ましくありません

※急ぎですので、レスポンスよく返せる方を希望します。

※写真等は何もないのですが、月末には写真素材が届きます。写真素材を使うデザインの場合取り急ぎ、別の素材で代用してください
ロゴのaiデータです

秀逸です

ありがとうございます

```html
<!DOCTYPE html>
<html lang="ja">
<head>
<meta charset="utf-8">
<title>KASANE Grand Open</title>
<link rel="stylesheet" href="https://fonts.googleapis.com/css2?family=Playfair+Display:ital,wght@0,700;1,700;1,900&family=Shippori+Mincho:wght@500;700;800&display=swap">
<style>
:root{
  --bg:#141210;
  --bg-deep:#0a0908;
  --gold:#d8b66c;
  --gold-light:#f2dc9e;
  --gold-dark:#9c7a3a;
  --ink:#f5f1e8;
  --muted:#cfc7b6;
}
*{margin:0;padding:0;box-sizing:border-box}
html,body{width:849px;height:1200px;overflow:hidden;background:var(--bg-deep)}
body{font-family:"Shippori Mincho",serif;color:var(--ink)}
.flyer{position:relative;width:849px;height:1200px;overflow:hidden;
  background:linear-gradient(180deg,#1c1916 0%,var(--bg) 40%,var(--bg-deep) 100%)}
.gold-text{background:linear-gradient(180deg,var(--gold-light) 0%,var(--gold) 50%,var(--gold-dark) 100%);
  -webkit-background-clip:text;background-clip:text;color:transparent}

.header{position:absolute;top:30px;left:0;width:100%;display:flex;justify-content:center;align-items:center;gap:14px;font-size:26px;font-weight:700;color:var(--ink);line-height:1.2}
.header .brand-dot{width:14px;height:14px;border-radius:50%;background:var(--gold)}
.header .brand{font-family:"Playfair Display",serif;letter-spacing:3px}

.headline{position:absolute;top:112px;width:100%;text-align:center;font-family:"Playfair Display",serif;font-style:italic;font-weight:900;font-size:100px;letter-spacing:2px;line-height:1.05;white-space:nowrap}

.concept{position:absolute;top:248px;left:34px;height:84px;display:flex;align-items:center;gap:14px;white-space:nowrap;z-index:2}
.concept .tag{border:2px solid var(--gold);padding:2px 14px;font-size:44px;font-weight:800;color:var(--ink);line-height:1.3}
.concept .bar{font-family:"Playfair Display",serif;font-weight:700;font-size:82px;line-height:1;margin-top:-12px}
.concept .times{font-size:50px;color:var(--gold)}
.concept .yakiniku{font-size:74px;font-weight:800;line-height:1}

.date{position:absolute;top:250px;right:28px;width:150px;border:2px solid var(--gold);text-align:center;background:rgba(0,0,0,.55);z-index:2}
.date .day{font-family:"Playfair Display",serif;font-size:46px;font-weight:700;line-height:1.15;padding-top:2px}
.date .time{background:var(--gold);color:var(--bg-deep);font-size:22px;font-weight:800;line-height:1.4;padding:2px 0;white-space:nowrap}

.photo-interior{position:absolute;top:336px;left:0;width:849px;height:360px;
  background:linear-gradient(160deg,#2a2f45 0%,#1a1d2c 35%,#3a2a22 70%,#1a1512 100%)}
.lead{position:absolute;top:350px;left:462px;height:420px;writing-mode:vertical-rl;font-size:24px;font-weight:700;line-height:1.6;color:var(--ink);text-shadow:0 0 8px rgba(0,0,0,.9);z-index:3}

.photo-meat{position:absolute;top:640px;left:0;width:470px;height:340px;
  clip-path:polygon(0 8%,100% 0,90% 100%,0 100%);
  background:radial-gradient(ellipse at 40% 45%,#b8414a 0%,#8a2a30 45%,#3a1214 100%)}
.photo-drinks{position:absolute;top:680px;left:470px;width:379px;height:300px;
  background:radial-gradient(ellipse at 50% 60%,#4a7fb0 0%,#c88a3a 45%,#1a1512 85%)}

.floor-badge{position:absolute;top:900px;left:8px;width:124px;height:124px;border-radius:50%;border:2px solid var(--gold);background:var(--bg-deep);display:flex;flex-direction:column;justify-content:center;align-items:center;z-index:2}
.floor-badge .label{font-size:19px;font-weight:700;line-height:1.3}
.floor-badge .value{font-size:46px;font-weight:800;line-height:1.1}
.floor-badge .value small{font-size:24px}

.features{position:absolute;top:992px;left:142px;display:flex;gap:10px;z-index:2}
.features li{list-style:none;border:2px solid var(--gold);padding:6px 14px;font-size:23px;font-weight:800;line-height:1.3;white-space:nowrap;color:var(--gold-light);background:rgba(10,9,8,.9)}

.footer{position:absolute;top:1062px;left:0;width:100%;height:138px;border-top:1px solid var(--gold-dark)}
.footer .logo{position:absolute;top:22px;left:26px;display:flex;flex-direction:column;align-items:center;gap:10px}
.footer .logo .mark{width:46px;height:46px;border-radius:50%;background:var(--gold)}
.footer .logo .name{font-family:"Playfair Display",serif;font-size:18px;letter-spacing:3px;color:var(--gold)}
.info{position:absolute;top:16px;left:150px;font-size:22px;line-height:1.5;color:var(--ink);white-space:nowrap}
.info .key{color:var(--gold)}
.info .address{font-size:16px;color:var(--muted);margin-top:4px}
.contact{position:absolute;top:14px;left:510px;color:var(--ink);white-space:nowrap}
.contact .tel{font-size:34px;font-weight:700;line-height:1.2}
.contact .fax{font-size:20px;color:var(--muted);line-height:1.4}
.contact .search{margin-top:6px;display:flex;align-items:center;width:300px;border:1px solid var(--muted)}
.contact .search span{flex:1;padding:2px 8px;font-size:15px;background:var(--ink);color:var(--bg-deep)}
.contact .search b{padding:2px 10px;font-size:14px;background:var(--gold-dark);color:var(--ink)}
</style>
</head>
<body>
<div class="flyer">
  <div class="header"><span>高級焼肉bar</span><span class="brand-dot"></span><span class="brand">KASANE</span></div>

  <h1 class="headline gold-text">GRAND OPEN</h1>

  <div class="concept">
    <span class="tag">新感覚</span>
    <span class="bar">bar</span>
    <span class="times">×</span>
    <span class="yakiniku">焼肉</span>
  </div>

  <div class="date">
    <div class="day gold-text">7/4</div>
    <div class="time">土 18:00</div>
  </div>

  <div class="photo-interior" role="img" aria-label="照明の灯る高級バーの店内写真"></div>
  <div class="photo-meat" role="img" aria-label="霜降り和牛の焼肉写真"></div>
  <div class="photo-drinks" role="img" aria-label="色鮮やかなカクテルのグラス写真"></div>

  <p class="lead">高級感漂うゴージャスなバーで<br>焼肉メニューを楽しむことができます</p>

  <div class="floor-badge">
    <span class="label">店内面積</span>
    <span class="value gold-text">40<small>坪</small></span>
  </div>

  <ul class="features">
    <li>バーカウンター</li>
    <li>ボックス席</li>
    <li>カラオケ付きVIPルーム有</li>
  </ul>

  <footer class="footer">
    <div class="logo"><span class="mark"></span><span class="name">KASANE</span></div>
    <div class="info">
      <p><span class="key">[営業時間]</span>18:00～05:00</p>
      <p><span class="key">[休　日]</span>日曜</p>
      <p class="address">愛知県名古屋市中区錦9-8-7 月灯ビル2F</p>
    </div>
    <div class="contact">
      <p class="tel">Tel:052-000-4521</p>
      <p class="fax">Fax:052-000-4522</p>
      <div class="search"><span>KASANE</span><b>検索</b></div>
    </div>
  </footer>
</div>
</body>
</html>
```